pvt business card

need clean and modern business card design, possibly two. Logo on front and writing on back-Full source files for logo attached-THE CHOSEN LOGO IS SQUARE PVT with PVT HOLDINGS in ALL BLUE. Please do not use any other logos from files, this is source file that includes correct logo

```html
<!DOCTYPE html>
<html lang="en">
<head>
<meta charset="utf-8">
<title>PVT Holdings Business Card</title>
<link rel="stylesheet" href="https://fonts.googleapis.com/css2?family=Roboto:wght@400;500;700&display=swap">
<style>
  :root {
    --backdrop: #2b2b2c;
    --card-black: #141415;
    --card-black-edge: #1c1c1e;
    --brand-blue: #1f7fe0;
    --band-blue: #1d86ea;
    --ink-dark: #0d1a2a;
    --title-grey: #c4c4c4;
    --silver: #d2d4d6;
  }
  * { margin: 0; padding: 0; box-sizing: border-box; }
  html, body {
    width: 1200px;
    height: 900px;
    overflow: hidden;
    background: var(--backdrop);
    font-family: "Roboto", Arial, sans-serif;
  }
  .stage {
    position: relative;
    width: 1200px;
    height: 900px;
  }
  .card {
    position: absolute;
    top: 305px;
    width: 500px;
    height: 290px;
    border-radius: 22px;
    overflow: hidden;
    background: var(--card-black);
    box-shadow: 0 14px 30px rgba(0, 0, 0, 0.45);
  }
  .card--info { left: 70px; }
  .card--brand { left: 630px; background: var(--card-black-edge); }

  .brand-lockup {
    display: flex;
    align-items: center;
    justify-content: center;
    gap: 12px;
  }
  .brand-square {
    width: 22px;
    height: 22px;
  }
  .brand-name {
    font-weight: 500;
    letter-spacing: 2px;
  }

  .card--info .brand-lockup { margin-top: 38px; }
  .card--info .brand-square { background: var(--brand-blue); }
  .card--info .brand-name { color: var(--brand-blue); font-size: 28px; }

  .person {
    text-align: center;
    margin-top: 18px;
  }
  .person-name {
    color: var(--brand-blue);
    font-weight: 700;
    font-size: 19px;
    letter-spacing: 0.5px;
  }
  .person-title {
    color: var(--title-grey);
    font-size: 13px;
    letter-spacing: 0.8px;
    margin-top: 2px;
  }

  .contact-band {
    position: absolute;
    left: 0;
    right: 0;
    bottom: 0;
    height: 108px;
    background: var(--band-blue);
    display: flex;
    flex-direction: column;
    justify-content: center;
    align-items: center;
    gap: 8px;
    color: var(--ink-dark);
    font-size: 14.5px;
  }
  .contact-line span + span::before {
    content: "|";
    margin: 0 9px;
  }

  .card--brand .brand-lockup {
    flex-direction: column;
    height: 100%;
    gap: 22px;
  }
  .card--brand .brand-square {
    width: 56px;
    height: 56px;
    background: var(--silver);
  }
  .card--brand .brand-name { color: var(--silver); font-size: 30px; }
</style>
</head>
<body>
<main class="stage">
  <section class="card card--info" aria-label="Business card, contact side">
    <div class="brand-lockup">
      <div class="brand-square"></div>
      <div class="brand-name">PVT HOLDINGS</div>
    </div>
    <div class="person">
      <div class="person-name">DARA WHITLOW</div>
      <div class="person-title">MANAGING DIRECTOR</div>
    </div>
    <div class="contact-band">
      <div class="contact-line"><span>738, Harbor Lane North Fieldtown, 58213</span></div>
      <div class="contact-line"><span>555 013 7429</span><span>hello@pvtmail.com</span><span>www.pvtholdings.com</span></div>
    </div>
  </section>

  <section class="card card--brand" aria-label="Business card, brand side">
    <div class="brand-lockup">
      <div class="brand-square"></div>
      <div class="brand-name">PVT HOLDINGS</div>
    </div>
  </section>
</main>
</body>
</html>
```